Elegant wine label

Looking for a new Napa Valley wine label called "Velmora". Our wines will retail for $150 + per bottle. Velmora is derived from the greek word Ergo (therefore) tied in with Air for aeration for wine.

We handcraft our small production wine. 200 cases.
Looking for a very sophisticated, minimalist elegant look. Wine labels we like for inspiration and reference include: www.tarvik.wine, www.pellunwine.com, www.morvadestates.com, www.quillbarrowwine.com, www.brevixestate.com/Wine, https://shop.lantivewine.com/wine

Colors will include white, black and blue foil (Approx. color: C 94.9, M 83.53, Y 0, K 0). We want a custom-created, minimal greek/roman looking font for lettering.

```html
<!DOCTYPE html>
<html lang="en">
<head>
<meta charset="UTF-8">
<title>Velmora — Napa Valley Cabernet Sauvignon Label</title>
<link rel="stylesheet" href="https://fonts.googleapis.com/css2?family=Bodoni+Moda:opsz,wght@6..96,400;6..96,500&display=swap">
<style>
  :root {
    --page: #ffffff;
    --label-dark: #26272d;
    --label-mid: #2f3037;
    --label-light: #3b3b44;
    --ink-white: #ffffff;
    --ink-muted: #b4b5c0;
    --foil-blue: #3a4bd8;
  }
  html, body {
    margin: 0;
    padding: 0;
    width: 675px;
    height: 1200px;
    overflow: hidden;
    background: var(--page);
  }
  .canvas {
    position: relative;
    width: 675px;
    height: 1200px;
  }
  .label {
    position: absolute;
    left: 67px;
    top: 233px;
    width: 540px;
    height: 733px;
    background: linear-gradient(100deg, var(--label-dark) 0%, var(--label-mid) 55%, var(--label-light) 100%);
    font-family: "Bodoni Moda", "Didot", serif;
    text-align: center;
  }
  .appellation,
  .varietal,
  .vintage {
    position: absolute;
    left: 0;
    width: 100%;
    margin: 0;
    color: var(--ink-muted);
    font-weight: 500;
    text-transform: uppercase;
  }
  .appellation {
    top: 82px;
    font-size: 14px;
    line-height: 27px;
    letter-spacing: 0.22em;
  }
  .wordmark {
    position: absolute;
    left: 0;
    top: 318px;
    width: 100%;
    margin: 0;
    color: var(--ink-white);
    font-weight: 400;
    font-size: 98px;
    line-height: 100px;
    letter-spacing: -0.01em;
  }
  .foil-rule {
    position: absolute;
    left: 77px;
    top: 428px;
    width: 387px;
    height: 6px;
  }
  .varietal {
    top: 550px;
    font-size: 19px;
    line-height: 34px;
    letter-spacing: 0.2em;
  }
  .vintage {
    top: 655px;
    font-size: 19px;
    letter-spacing: 0.3em;
  }
</style>
</head>
<body>
<main class="canvas">
  <section class="label" aria-label="Velmora wine label">
    <p class="appellation">Napa Valley<br>California</p>
    <h1 class="wordmark">Velmora</h1>
    <svg class="foil-rule" viewBox="0 0 387 6" aria-hidden="true">
      <defs>
        <linearGradient id="foil-left" x1="0" x2="1" y1="0" y2="0">
          <stop offset="0" stop-color="#3a4bd8"/>
          <stop offset="1" stop-color="#3a4bd8" stop-opacity="0.15"/>
        </linearGradient>
        <linearGradient id="foil-right" x1="0" x2="1" y1="0" y2="0">
          <stop offset="0" stop-color="#3a4bd8" stop-opacity="0.3"/>
          <stop offset="1" stop-color="#3a4bd8"/>
        </linearGradient>
      </defs>
      <rect x="0" y="1" width="193" height="3" fill="url(#foil-left)"/>
      <rect x="328" y="1" width="59" height="3" fill="url(#foil-right)"/>
    </svg>
    <p class="varietal">Cabernet<br>Sauvignon</p>
    <p class="vintage">2025</p>
  </section>
</main>
</body>
</html>
```